Business Improvement Consultancy needs web design

I need a web design for my company, that offers support to manufacturing and distribution businesses.

We have worked with a range of organisations to help them get more out of their operational processes and supply chains.

With full end to end supply chain knowledge we help them identify waste in their supply chains that often get overlooked.

We support through a number of offerings

Developing an end to end supply chain strategy

Applying Lean to support the strategy

Interim support network to deliver quick wins and rapid cost improvement

Project Management

Interactive training tools for delivering supply chain best practice.

I have the logos done already, so it is more about look and feel, and the colour schemes etc giving a professional feel.

Also have the web domains www.veltrisgroup.co, www.veltrisgroup.co.uk & www.veltrisgroup.eu, using Q&Z beginner package

Target Market(s)

Manufacturing and distribution businesses, potentially other consultancies looking for collaboration

Industry/Entity Type

Business

Requirements
Must have
• Some pictures on related to performance improvement, bar charts showing productivity growth / increase.

Should have the facebook twitter and linkedin logos to share the website

```html
<!DOCTYPE html>
<html lang="en">
<head>
<meta charset="utf-8">
<title>Veltris Group – Supply Chain &amp; Lean Consultancy</title>
<link rel="stylesheet" href="https://fonts.googleapis.com/css2?family=Ubuntu:wght@400;500&display=swap">
<style>
  :root {
    --brand-navy: #2b2a6a;
    --brand-blue: #1aa6f0;
    --brand-blue-dark: #0b8ee0;
    --text-dark: #1c1c1c;
    --text-body: #333333;
    --frame-line: #cccccc;
    --card-bg: #f2f2f2;
    --hero-bg: #e4e4e4;
    --button-bg: #33373b;
    --footer-bg: #373a3e;
    --white: #ffffff;
  }
  * { box-sizing: border-box; margin: 0; padding: 0; }
  html, body { width: 876px; height: 1200px; overflow: hidden; background: var(--white); }
  body { position: relative; font-family: "Ubuntu", "Trebuchet MS", sans-serif; color: var(--text-dark); }

  /* Header */
  .brand { position: absolute; left: 34px; top: 20px; display: flex; align-items: center; gap: 14px; }
  .brand-mark { width: 26px; height: 26px; border-radius: 50%; background: var(--brand-navy); }
  .brand-name { font-size: 21px; font-weight: 400; color: var(--brand-navy); }

  .main-nav { position: absolute; left: 263px; top: 0; height: 66px; }
  .main-nav a { position: absolute; top: 0; height: 66px; line-height: 106px; font-size: 14px; color: var(--text-dark); text-decoration: none; white-space: nowrap; }
  .main-nav a.is-active { width: 80px; left: 0; text-align: center; color: var(--white); background: linear-gradient(var(--brand-blue), var(--brand-blue-dark)); }

  /* Page frame */
  .page-frame { position: absolute; left: 19px; top: 101px; width: 828px; height: 979px; border: 1px solid var(--frame-line); }

  /* Hero */
  .hero { position: absolute; left: 37px; top: 110px; width: 791px; height: 305px; background: var(--hero-bg); }
  .hero-visual { position: absolute; left: 9px; top: 8px; width: 524px; height: 289px;
    background: linear-gradient(160deg, #ffffff 0%, #f1f1f1 45%, #d8dadc 100%); }
  .hero-visual::after { content: ""; position: absolute; left: 120px; top: 80px; width: 260px; height: 150px;
    background: linear-gradient(90deg, #d82020, #e8a010 45%, #b8d020 70%, #20c020); opacity: .35; border-radius: 4px; }
  .hero-panel { position: absolute; left: 533px; top: 8px; width: 251px; height: 289px;
    background: linear-gradient(#25b4f6, #0a8ddf); color: var(--white); padding: 26px 22px 0 22px; }
  .hero-title { font-size: 26px; font-weight: 500; line-height: 33px; }
  .hero-text { margin-top: 12px; font-size: 13.5px; line-height: 18px; }
  .hero-dots { position: absolute; left: 33px; top: 255px; display: flex; gap: 5px; }
  .hero-dots span { width: 14px; height: 14px; border-radius: 50%; background: var(--white); }
  .hero-dots span.is-current { background: #1d1d1d; }

  /* Cards */
  .card { position: absolute; top: 427px; height: 316px; background: var(--card-bg); border: 1px solid var(--frame-line); }
  .card-solutions { left: 38px; width: 254px; }
  .card-about { left: 299px; width: 263px; }
  .card-practice { left: 569px; width: 261px; }
  .card-title { position: absolute; top: 14px; font-size: 26px; font-weight: 400; }
  .card-photo { position: absolute; top: 53px; width: 216px; height: 108px; }
  .card-solutions .card-photo { left: 15px; background: linear-gradient(120deg, #1e1e22 0%, #6e6a66 55%, #cfcfd0 100%); }
  .card-about .card-photo { left: 23px; background: linear-gradient(120deg, #e6e2de 0%, #9aa0a8 50%, #2c3038 100%); }
  .card-text { position: absolute; top: 175px; width: 210px; font-size: 10.5px; line-height: 14.5px; color: var(--text-body); }
  .read-more { position: absolute; top: 264px; width: 96px; height: 32px; line-height: 32px; text-align: center;
    background: var(--button-bg); color: var(--white); font-size: 11px; text-decoration: none; border: 2px solid #f8f8f8; outline: 1px solid #bbb; }

  .practice-list { position: absolute; left: 10px; top: 54px; width: 240px; list-style: none; }
  .practice-list li { position: relative; padding-left: 16px; font-size: 10.5px; line-height: 14.5px; color: var(--text-body); margin-bottom: 16px; }
  .practice-list li::before { content: ""; position: absolute; left: 2px; top: 3px; width: 8px; height: 8px; border-radius: 50%; background: var(--brand-blue-dark); }

  /* Welcome */
  .welcome { position: absolute; left: 42px; top: 793px; width: 770px; }
  .welcome-title { font-size: 43px; font-weight: 400; line-height: 50px; }
  .welcome-text { margin-top: 8px; font-size: 17.5px; line-height: 24px; color: #111; }

  /* Footer */
  .site-footer { position: absolute; left: 20px; top: 1087px; width: 826px; height: 113px; background: var(--footer-bg); }
  .share-links { position: absolute; left: 41px; top: 20px; display: flex; flex-direction: column; gap: 6px; }
  .share-links span { width: 19px; height: 19px; border-radius: 4px; background: #8ab8d8; }
</style>
</head>
<body>
  <header>
    <div class="brand"><span class="brand-mark"></span><span class="brand-name">Veltris Group</span></div>
    <nav class="main-nav">
      <a class="is-active" href="#">Home</a>
      <a href="#" style="left:121px">Supply Chain</a>
      <a href="#" style="left:263px">Lean</a>
      <a href="#" style="left:343px">Interim</a>
      <a href="#" style="left:447px">Contact Us</a>
    </nav>
  </header>

  <div class="page-frame"></div>

  <section class="hero">
    <div class="hero-visual" role="img" aria-label="3D bar chart with rising arrow showing productivity growth"></div>
    <div class="hero-panel">
      <h1 class="hero-title">Support to manufacturing and distribution businesses.</h1>
      <p class="hero-text">Help them to get more out of their operational processes and supply chains.</p>
      <div class="hero-dots"><span class="is-current"></span><span></span><span></span><span></span></div>
    </div>
  </section>

  <section class="card card-solutions">
    <h2 class="card-title" style="left:22px">Solutions</h2>
    <div class="card-photo" role="img" aria-label="Business team meeting in an office"></div>
    <p class="card-text" style="left:17px">Tailored end to end supply chain strategy and lean programmes that deliver lasting results……</p>
    <a class="read-more" href="#" style="left:11px">READ MORE</a>
  </section>

  <section class="card card-about">
    <h2 class="card-title" style="left:30px">Who We Are</h2>
    <div class="card-photo" role="img" aria-label="Consultancy team working together at a desk"></div>
    <p class="card-text" style="left:25px">An experienced team of supply chain and operations specialists working alongside your people……</p>
    <a class="read-more" href="#" style="left:26px">READ MORE</a>
  </section>

  <section class="card card-practice">
    <h2 class="card-title" style="left:23px">Practice</h2>
    <ul class="practice-list">
      <li>Interim support network delivering quick wins and rapid cost improvement across your operations……</li>
      <li>Project management that keeps improvement plans on time, on budget and fully aligned……</li>
      <li>Interactive training tools that bring supply chain best practice to every level of staff……</li>
    </ul>
  </section>

  <section class="welcome">
    <h2 class="welcome-title">Welcome Dear Visitor!</h2>
    <p class="welcome-text">Welcome to Veltris Group. We have worked with a range of organisations to help them get more out of their operational processes and supply chains.With full end to end supply chain knowledge we can help you identify waste in your supply chains that often get overlooked. Before you look to embark on cost reduction plans or a lean journey, get in touch to ensure that your chosen path delivers sustainability and profitable growth.</p>
  </section>

  <footer class="site-footer">
    <div class="share-links" aria-label="Share links"><span></span><span></span><span></span></div>
  </footer>
</body>
</html>
```